Qorvex app promo Web page

Vantel Forge Project Description / Qorvex App Website

Project: Website / Basic / For an Qorvex app promo with a company logo revision

Purpose: Provide a public “Face” for a new Qorvex app, promoting the app and having a link to the Brimzo store.

Depth: 2 levels: Level 1 - Home page / Level 2: Media, Contact, About, Blog (all 1-page) (5 pages in all)(Button pages will be similar and simple.

Navigation: Home page: Button: Brimzo store link, Media, Contact, About, Blog

Design style: The Web design can go one of two ways - directly reflect the app Style design or have a clean, dramatic, “European” design with a white or black background. The second approach is probably the best way, as we may use this website to feature other apps as well.

Home page: See attached page with elements for design of art / copy / buttons. Also, I attach some app web pages that can help inform the designer's appreciation for what we want.

Media Page See attached rough layout of art

Contact See attached file

About See attached file

Blog See attached file

Reason: I am traveling and need to review everyone's work more extensively plan to co,plete and decide over the weekend. .

Reason: My business trip was extended - need the time to review designs with my partner.I will send feedback to designers, though - later tonight.

Target Market(s)

Adults with smart phones (Aged 18-45) & media visitors

Industry/Entity Type

Store

Requirements
Must have
• Attached information on page contents...

Home page:
- Company logo
- Qorvex app icon and name
- Product description
- Features list
- Button to go to Brimzo Store
- Buttons to go to other pages: Media, Contact, About, Blog

Media page:
- Company logo
- List of media downloads (Releases, backgrounder, etc.)
- Return to home button

Contact page:
- Company logo
- E-mail structure for inputting name, e-mail, and message

About:
- Company logo
- Space for copy on company / and app

Blog:
- Company logo
- Space for blog to appear

Nice to have
• I have attached a few other site designs to show the elegance and strong design we would like.

We do have a company logo approach that will need to be tweaked a bit.

I would like to see a clean design that allows the app to be featured but will be distinctive in its own right. We want to be seen as a very contemporary, clean, sleek, elegant design type company.
Should not have
• Not too cluttered of a design.

```html
<!DOCTYPE html>
<html lang="en">
<head>
<meta charset="utf-8">
<title>About — ZORVALI Health Resources, LLC</title>
<link href="https://fonts.googleapis.com/css2?family=Source+Sans+3:wght@400;600;700&display=swap" rel="stylesheet">
<style>
:root{
  --page-bg:#e6e6e6;
  --panel:#ffffff;
  --ink:#111111;
  --nav-ink:#666666;
  --nav-active:#111111;
  --accent-red:#c8201f;
  --brand-green:#5bb53a;
  --dark:#2f2f2f;
  --darker:#1d1d1d;
  --social-blue:#1d8ed6;
  --divider:#cfcfcf;
}
*{margin:0;padding:0;box-sizing:border-box}
html,body{width:1200px;height:813px;overflow:hidden}
body{background:var(--page-bg);font-family:"Source Sans 3",sans-serif;color:var(--ink);position:relative}
.top-strip{position:absolute;left:0;top:0;width:1200px;height:14px;background:linear-gradient(#474747,#333)}
.brand{position:absolute;left:178px;top:25px;height:53px;display:flex;align-items:center;gap:9px}
.brand-dot{width:50px;height:50px;border-radius:50%;background:var(--brand-green);flex:none}
.brand-name{font-size:21px;font-weight:400;color:#222}
.main-nav{position:absolute;left:555px;top:32px;display:flex}
.main-nav a{display:flex;align-items:center;width:91px;height:42px;padding-left:6px;border-left:1px dotted var(--divider);font-size:12px;font-weight:700;color:var(--nav-ink);text-decoration:none;text-transform:uppercase}
.main-nav a:last-child{border-right:1px dotted var(--divider)}
.main-nav a::before{content:"›";font-size:15px;margin-right:4px;color:var(--nav-ink)}
.main-nav a.is-active{color:var(--nav-active)}
.main-nav a.is-active::before{color:var(--accent-red)}
.content-panel{position:absolute;left:170px;top:88px;width:857px;height:546px;background:var(--panel)}
.hero-photo{position:absolute;left:19px;top:50px;width:304px;height:331px;background:radial-gradient(circle at 60% 35%,#f7f1dc,#d9cf9c 55%,#b8b27a)}
.title-band{position:absolute;left:342px;top:50px;width:499px;height:82px;background:linear-gradient(90deg,#3a3a3a,#0a0a0a 70%,#000);display:flex;align-items:center;padding-left:21px;gap:12px}
.title-band .brand-dot{width:58px;height:58px}
.title-band .brand-name{color:#fff;font-size:25px}
.about-copy{position:absolute;left:362px;top:159px;width:400px;font-size:12.2px;line-height:14.4px}
.about-copy p+p{margin-top:14.4px}
.social-tabs{position:absolute;left:1027px;top:111px;display:flex;flex-direction:column;gap:2px}
.social-tabs span{display:flex;align-items:center;justify-content:center;width:26px;height:30px;background:var(--social-blue);border-radius:0 4px 4px 0;color:#fff;font-size:7px;font-weight:600}
.social-tabs span:first-child{height:48px}
.footer-links{position:absolute;left:0;top:657px;width:1200px;height:121px;background:var(--dark);padding:12px 0 0 199px}
.footer-links a{display:block;color:#fff;font-size:11.5px;font-weight:700;text-decoration:none;line-height:22.3px}
.footer-bottom{position:absolute;left:0;top:778px;width:1200px;height:35px;background:var(--darker);border-top:1px solid #3c3c3c;color:#fff;font-size:10px;text-align:center;line-height:34px}
</style>
</head>
<body>
<div class="top-strip"></div>
<header class="brand"><span class="brand-dot"></span><span class="brand-name">ZORVALI Health Resources, LLC</span></header>
<nav class="main-nav">
  <a href="#">Home</a><a href="#" class="is-active">About</a><a href="#">Media</a><a href="#">Blog</a><a href="#">Contact</a>
</nav>
<main class="content-panel">
  <div class="hero-photo" role="img" aria-label="Photo of a smiling woman in a sunlit field"></div>
  <div class="title-band"><span class="brand-dot"></span><span class="brand-name">ZORVALI Health Resources, LLC</span></div>
  <section class="about-copy">
    <p><strong>Welcome to Savanna Trails Online,</strong> the experts in planning and delivering bespoke African Safaris to customers all over the world. Africa has caught the imagination of travellers for centuries and for good reason, she is a breathtaking continent at every turn with some of the most incredible scenery, wildlife and culture anywhere on the planet.</p>
    <p>Africa has really got something to offer everybody and our job is to tailor each safari to meet our clients expectations exactly, however luxurious or adventur-ous. We have organised once in lifetime honeymoons where clients have enjoyed 5 star lodges in the Masai Mara with a dawn hot air balloon trip then hopped on a light aircraft and spent the remainder of the trip relaxing on a private beach in Zanzibar, the spice island. For the more adventurous, we have led gruelling fishing safaris to the isolated and desolate Lake Turkana in search of the legendary Nile perch, seeing some of the more colourful African tribes along the way.</p>
  </section>
</main>
<div class="social-tabs"><span>Linko</span><span>Pipit</span></div>
<footer class="footer-links">
  <a href="#">Home</a><a href="#">About</a><a href="#">Media</a><a href="#">Blog</a><a href="#">Contact</a>
</footer>
<div class="footer-bottom">© Copyright 2013 . All rights reserved&nbsp; ZORVALI Health Resources, LLC.</div>
</body>
</html>
```